Vitalora Poster

Please see attached file, would like it similar to this using our own photos and changing images a bit. This is an Vitalora poster, healthy, fitness, weight loss, wealth creation, stress relief, energy.

Industry/Entity Type

Weight

Colors
acd037
fece3e
34a7d8
85acd3
34b8a5

```html
<!DOCTYPE html>
<html lang="en">
<head>
<meta charset="utf-8">
<title>Vitalora Poster</title>
<link href="https://fonts.googleapis.com/css2?family=Anton&family=Arimo:wght@400;700&display=swap" rel="stylesheet">
<style>
  :root {
    --green: #4a9b2f;
    --grey-text: #9a9a9a;
    --ink: #2b2b2b;
    --paper: #ffffff;
    --rule: #555555;
  }
  * { margin: 0; padding: 0; box-sizing: border-box; }
  html, body { width: 844px; height: 1200px; overflow: hidden; background: var(--paper); }
  .poster {
    position: relative;
    width: 844px;
    height: 1200px;
    background: var(--paper);
    font-family: "Arimo", Arial, sans-serif;
  }
  .top-rule {
    position: absolute; left: 0; top: 6px; width: 697px; height: 1px;
    background: var(--rule);
  }
  .hero-photo {
    position: absolute; left: 0; top: 40px; width: 462px; height: 1109px;
    background: linear-gradient(180deg, #f4f4f4 0%, #d9c2b4 18%, #b9bcc0 38%, #c7ced6 55%, #e2b9a0 66%, #8aa6c6 82%, #6f8fb8 100%);
  }
  .headline {
    position: absolute; left: 465px; top: 28px;
    font-family: "Anton", Impact, sans-serif;
    font-weight: 400;
    font-size: 146px; line-height: 138px;
    color: var(--green);
    text-transform: uppercase;
    transform: scaleX(1.22);
    transform-origin: left top;
  }
  .headline span { display: block; height: 138px; }
  .benefits {
    position: absolute; left: 462px; top: 580px;
    list-style: none;
  }
  .benefits li {
    font-weight: 700; font-size: 19px; line-height: 31px;
    color: var(--grey-text);
    padding-left: 16px; position: relative;
  }
  .benefits li::before {
    content: ""; position: absolute; left: 0; top: 11px;
    width: 8px; height: 8px; background: var(--green);
  }
  .system-line {
    position: absolute; left: 462px; top: 782px;
    font-weight: 700; font-size: 19px; line-height: 24px;
    color: var(--green);
  }
  .brand {
    position: absolute; left: 458px; top: 904px; width: 370px;
  }
  .brand-role {
    display: block; text-align: right; padding-right: 26px;
    font-size: 12px; letter-spacing: 2px; color: var(--ink);
  }
  .brand-name {
    display: flex; align-items: center; gap: 12px;
    font-weight: 700; font-size: 62px; line-height: 66px; color: var(--ink);
    text-transform: uppercase;
  }
  .brand-dot {
    width: 20px; height: 20px; border-radius: 50%; background: var(--green);
  }
  .brand-tagline {
    display: block; margin-top: 4px;
    font-weight: 700; font-size: 17px; color: var(--ink);
  }
  .footer-band {
    position: absolute; left: 0; bottom: 0; width: 844px; height: 51px;
    background: var(--green);
    display: flex; align-items: center; justify-content: center;
    color: var(--paper); font-weight: 700; font-size: 17px;
  }
  .footer-band span + span::before {
    content: ""; display: inline-block; width: 4px; height: 22px;
    background: var(--ink); margin: 0 5px; vertical-align: -5px;
  }
</style>
</head>
<body>
  <div class="poster">
    <div class="top-rule"></div>
    <div class="hero-photo" role="img" aria-label="Photo of a smiling woman in a grey t-shirt and jeans pointing forward while measuring her waist with a yellow tape measure"></div>

    <h1 class="headline"><span>Do</span><span>You</span><span>Want</span><span>To?</span></h1>

    <ul class="benefits">
      <li>RELEASE STUBBORN FAT</li>
      <li>GAIN LEAN MUSCLE</li>
      <li>INCREASE YOUR ENERGY</li>
      <li>BOOST MENTAL CLARITY</li>
      <li>FEEL LESS STRESSED</li>
      <li>SLEEP SOUNDLY</li>
    </ul>

    <p class="system-line">NUTRITIONAL REPLENISHING<br>SYSTEM FOR OPTIMAL HEALTH</p>

    <div class="brand">
      <span class="brand-role">INDEPENDENT ASSOCIATE</span>
      <div class="brand-name"><span class="brand-dot"></span>Vitalora</div>
      <span class="brand-tagline">World Leader in Nutritional Cleansing</span>
    </div>

    <div class="footer-band">
      <span>HEALTHY</span><span>FITNESS</span><span>WEIGHT LOSS</span><span>WEALTH CREATION</span><span>STRESS RELIEF</span><span>ENERGY</span>
    </div>
  </div>
</body>
</html>
```